Custom Label for Women's Supplement Brand

Need a product label for our products, we have a logo designed but need to incorporate it in to our product line which will have capsule bottles, tincture bottles, and eventually skin care. We originally wanted a label that had black as main color, but are open to options. Want it to be sleek, and pull the eye, simple yet fun. Even something different that doesn’t look like anyone else.
Updates

Low designer entries

Target Market(s)

Women 26-70

Requirements
Nice to have
• Would love some metallic accents

```html
<!DOCTYPE html>
<html lang="en">
<head>
<meta charset="utf-8">
<title>Supplement Label Line</title>
<link rel="stylesheet" href="https://fonts.googleapis.com/css2?family=Oswald:wght@400;500&family=Roboto+Condensed:wght@400;700&display=swap">
<style>
  :root {
    --backdrop: #0b0b0e;
    --metal: #dfe3e8;
    --metal-dim: #c9ced6;
    --band: #f4f4f2;
    --ink: #2a2a2e;
    --violet: #9a55c2;
    --red: #e5232b;
    --blue: #3447b0;
    --green: #3fae3c;
    --pink: #e0478f;
  }
  * { box-sizing: border-box; margin: 0; padding: 0; }
  html, body { width: 1200px; height: 469px; overflow: hidden; background: var(--backdrop); }
  .label-line {
    width: 1200px; height: 469px;
    display: flex; justify-content: center; align-items: center; gap: 22px;
  }
  .label {
    width: 214px; height: 290px;
    display: flex; flex-direction: column;
    color: var(--metal);
  }
  .label--wellness { --tone: var(--violet); }
  .label--multi    { --tone: var(--red); }
  .label--sleep    { --tone: var(--blue); }
  .label--immune   { --tone: var(--green); }
  .label--pms      { --tone: var(--pink); }

  .label__face {
    flex: 1; background: var(--tone);
    display: flex; flex-direction: column; align-items: center;
    padding-top: 22px;
  }
  .brand { display: flex; align-items: center; gap: 6px; margin-bottom: 4px; }
  .brand__dot { width: 12px; height: 12px; border-radius: 50%; background: var(--metal); }
  .brand__name {
    font-family: "Oswald", sans-serif; font-weight: 400; font-size: 15px;
    color: var(--metal); line-height: 1.15; text-align: center;
  }
  .brand__rule { width: 96px; height: 1px; background: var(--metal-dim); margin: 6px 0 20px; }
  .product {
    font-family: "Oswald", sans-serif; font-weight: 400; font-size: 15px;
    line-height: 1.4; letter-spacing: 0.2px; text-align: center; text-transform: uppercase;
  }
  .specs {
    display: flex; align-items: center; gap: 12px;
    margin-top: 14px; font-family: "Roboto Condensed", sans-serif;
  }
  .specs__form { font-size: 7px; line-height: 1.05; text-transform: uppercase; width: 42px; }
  .specs__divider { width: 1px; height: 24px; background: var(--metal-dim); }
  .specs__count { font-size: 10px; font-weight: 700; line-height: 1; }
  .specs__count small { display: block; font-size: 4px; font-weight: 400; }
  .category {
    margin-top: 12px; font-family: "Roboto Condensed", sans-serif;
    font-size: 7px; text-transform: uppercase; letter-spacing: 0.3px;
  }
  .label__band {
    height: 62px; background: var(--band);
    display: flex; flex-direction: column; justify-content: center; align-items: center; gap: 5px;
  }
  .claims { display: flex; gap: 16px; color: var(--tone); }
  .claims svg { width: 16px; height: 16px; display: block; }
  .claim-names {
    display: flex; gap: 7px; font-family: "Roboto Condensed", sans-serif;
    font-size: 5.5px; font-weight: 700; color: var(--ink);
  }
</style>
</head>
<body>
<svg width="0" height="0" style="position:absolute" aria-hidden="true">
  <defs>
    <symbol id="icon-vegan" viewBox="0 0 16 16"><path d="M3 2 L8 14 L13 2 L11 2 L8 10 L5 2 Z" fill="currentColor"/></symbol>
    <symbol id="icon-nongm" viewBox="0 0 16 16"><path d="M4 2 H12 V4 L8 8 L12 12 V14 H4 V12 L8 8 L4 4 Z" fill="none" stroke="currentColor" stroke-width="1.8"/></symbol>
    <symbol id="icon-gluten" viewBox="0 0 16 16"><path d="M8 14 V7 M8 8 C5 8 3 6 3 3 C6 3 8 5 8 8 Z M8 8 C11 8 13 6 13 3 C10 3 8 5 8 8 Z M8 7 C6 5 7 2 8 1 C9 2 10 5 8 7 Z" fill="currentColor" stroke="currentColor" stroke-width="1"/></symbol>
    <symbol id="icon-kosher" viewBox="0 0 16 16"><circle cx="8" cy="8" r="7" fill="currentColor"/></symbol>
    <symbol id="icon-gelatin" viewBox="0 0 16 16"><path d="M2 9 H14 M3 6 V12 M13 6 V12" stroke="currentColor" stroke-width="2" fill="none"/></symbol>
  </defs>
</svg>

<main class="label-line">
  <article class="label label--wellness">
    <div class="label__face">
      <div class="brand"><span class="brand__dot"></span><span class="brand__name">Bright Harmony Wellness</span></div>
      <div class="brand__rule"></div>
      <h2 class="product">Women's Complete Wellness<br>Gummies</h2>
      <div class="specs"><span class="specs__form">Soft Gel Gummies</span><span class="specs__divider"></span><span class="specs__count">60<small>PCS</small></span></div>
      <p class="category">Dietary Supplement</p>
    </div>
    <div class="label__band">
      <div class="claims"><svg><use href="#icon-vegan"/></svg><svg><use href="#icon-nongm"/></svg><svg><use href="#icon-gluten"/></svg><svg><use href="#icon-kosher"/></svg><svg><use href="#icon-gelatin"/></svg></div>
      <div class="claim-names"><span>Vegan</span><span>Non-GM</span><span>Gluten-Free</span><span>Kosher</span><span>Gelatin-Free</span></div>
    </div>
  </article>

  <article class="label label--multi">
    <div class="label__face">
      <div class="brand"><span class="brand__dot"></span><span class="brand__name">Bright Harmony Wellness</span></div>
      <div class="brand__rule"></div>
      <h2 class="product">Super Multi Vitamin<br>Gummies</h2>
      <div class="specs"><span class="specs__form">Soft Gel Gummies</span><span class="specs__divider"></span><span class="specs__count">60<small>PCS</small></span></div>
      <p class="category">Dietary Supplement</p>
    </div>
    <div class="label__band">
      <div class="claims"><svg><use href="#icon-vegan"/></svg><svg><use href="#icon-nongm"/></svg><svg><use href="#icon-gluten"/></svg><svg><use href="#icon-kosher"/></svg><svg><use href="#icon-gelatin"/></svg></div>
      <div class="claim-names"><span>Vegan</span><span>Non-GM</span><span>Gluten-Free</span><span>Kosher</span><span>Gelatin-Free</span></div>
    </div>
  </article>

  <article class="label label--sleep">
    <div class="label__face">
      <div class="brand"><span class="brand__dot"></span><span class="brand__name">Bright Harmony Wellness</span></div>
      <div class="brand__rule"></div>
      <h2 class="product">Super Sleep Booster<br>Gummies</h2>
      <div class="specs"><span class="specs__form">Soft Gel Gummies</span><span class="specs__divider"></span><span class="specs__count">60<small>PCS</small></span></div>
      <p class="category">Dietary Supplement</p>
    </div>
    <div class="label__band">
      <div class="claims"><svg><use href="#icon-vegan"/></svg><svg><use href="#icon-nongm"/></svg><svg><use href="#icon-gluten"/></svg><svg><use href="#icon-kosher"/></svg><svg><use href="#icon-gelatin"/></svg></div>
      <div class="claim-names"><span>Vegan</span><span>Non-GM</span><span>Gluten-Free</span><span>Kosher</span><span>Gelatin-Free</span></div>
    </div>
  </article>

  <article class="label label--immune">
    <div class="label__face">
      <div class="brand"><span class="brand__dot"></span><span class="brand__name">Bright Harmony Wellness</span></div>
      <div class="brand__rule"></div>
      <h2 class="product">Super Immune Booster<br>Gummies</h2>
      <div class="specs"><span class="specs__form">Soft Gel Gummies</span><span class="specs__divider"></span><span class="specs__count">60<small>PCS</small></span></div>
      <p class="category">Dietary Supplement</p>
    </div>
    <div class="label__band">
      <div class="claims"><svg><use href="#icon-vegan"/></svg><svg><use href="#icon-nongm"/></svg><svg><use href="#icon-gluten"/></svg><svg><use href="#icon-kosher"/></svg><svg><use href="#icon-gelatin"/></svg></div>
      <div class="claim-names"><span>Vegan</span><span>Non-GM</span><span>Gluten-Free</span><span>Kosher</span><span>Gelatin-Free</span></div>
    </div>
  </article>

  <article class="label label--pms">
    <div class="label__face">
      <div class="brand"><span class="brand__dot"></span><span class="brand__name">Bright Harmony Wellness</span></div>
      <div class="brand__rule"></div>
      <h2 class="product">Women's PMS Relief<br>Gummies</h2>
      <div class="specs"><span class="specs__form">Soft Gel Gummies</span><span class="specs__divider"></span><span class="specs__count">60<small>PCS</small></span></div>
      <p class="category">Dietary Supplement</p>
    </div>
    <div class="label__band">
      <div class="claims"><svg><use href="#icon-vegan"/></svg><svg><use href="#icon-nongm"/></svg><svg><use href="#icon-gluten"/></svg><svg><use href="#icon-kosher"/></svg><svg><use href="#icon-gelatin"/></svg></div>
      <div class="claim-names"><span>Vegan</span><span>Non-GM</span><span>Gluten-Free</span><span>Kosher</span><span>Gelatin-Free</span></div>
    </div>
  </article>
</main>
</body>
</html>
```